Infographic & Data Visualisation Design for – Australia’s Yearly Harmwatch Review 2026

About Callowmere Institute: Callowmere Institute is an independent non-profit public health organization. We produce Australia’s Yearly Harmwatch Review, which translates verified national mortality data into actionable insights for policymakers, journalists, healthcare workers, and the general public.

Project Goal: We need a suite of high-impact, clean, and authoritative infographics and data visualisations created for Australia’s Yearly Harmwatch Review 2026.

What We Are Providing:

Full Dataset (.xlsx): Complete Excel file containing all 2026 report data.

Data & Chart Guidance Doc (.docx): A summary document detailing each dataset, the core takeaway, and our initial recommendations for chart types (e.g., line graphs, horizontal bar charts, donut charts, metric tiles).

Callowmere Institute Brand Book (.pdf): Complete brand guidelines covering fonts, colors, line weights, and imagery. These guidelines and in particular colours should be used across the infographics.

Previous Year Reference: You can view how last year’s report and graphics here: https://www.callowmere-example.org.au/australias-yearly-harmwatch-review-2025/

Designer Input & Creative Freedom: While we have provided a guide suggesting specific chart types for each dataset, we are not data visualisation experts - you are! We are very open to your creative ideas, structural suggestions, and design expertise. If you identify a clearer, more engaging, or visually compelling way to illustrate a specific dataset, we welcome your input.

Required Deliverables:

Master Report Infographics: High-resolution, print/PDF-ready A4 vector graphics for the formal report publication (Delivered as vector AI/EPS and high-res PDF/PNG).

Web Assets: Web-optimized PNG/SVG files with transparent or brand backgrounds.

Social Media Adaptations: 1:1 (Square) and 4:5 / 9:16 (Vertical) graphic cards for Instagram, LinkedIn, Facebook, and X.
Updates

Deadline was too tight - have extended it to ensure the designers have enough time to do the job.

Target Market(s)

Policy makers, journalists, health sector professionals, frontline workers, and the general public.

Industry/Entity Type

Drug/Government/Not for Profit

Font styles to use
Sans Serif
Other font styles liked:
• Brand Fonts: Use any or a combination of: Host Grotesk or Libre Baskerville or Poppins or Calibri Light

Colors

Designer to choose colors to be used in the design.

Requirements
Must have
• The ability to create Infographics, graphs of all kinds from data that we have given.
Nice to have
• Help with choosing what infographics/graphs/donuts graphs etc will be best to visualise the data.
Should not have
• A designer who has not made graphs or infographics from Data.

```html
<!DOCTYPE html>
<html lang="en">
<head>
<meta charset="utf-8">
<title>Australia’s Yearly Harmwatch Review 2026 – Infographic Suite</title>
<link href="https://fonts.googleapis.com/css2?family=Host+Grotesk:wght@400;500;600;700&family=Libre+Baskerville:ital,wght@0,400;0,700;1,400&display=swap" rel="stylesheet">
<style>
:root{
  --board:#152a4e;
  --paper:#ffffff;
  --navy:#1a2a4d;
  --orange:#f47a40;
  --blue:#4389d0;
  --indigo:#5a66b3;
  --sky:#a8c3e3;
  --teal:#2b5470;
  --cyan:#79c7d6;
  --purple:#6a3b9c;
  --plum:#5b1c42;
  --green:#1f7a45;
  --charcoal:#2c2c38;
  --ink:#1d1d24;
  --grid:#9a9aa4;
  --track:#e4e4e8;
  --row-a:#e9f2fb;
  --row-b:#d8e7f4;
}
*{box-sizing:border-box;margin:0;padding:0}
html,body{width:1200px;height:1019px;overflow:hidden;background:var(--board)}
.board{
  position:absolute;left:39.3px;top:39.3px;
  display:grid;
  grid-template-columns:repeat(5,218.4px);
  grid-template-rows:repeat(3,308.5px);
  column-gap:7.6px;row-gap:7.4px;
}
.panel{background:var(--paper);width:218.4px;height:308.5px}
.panel svg{display:block;width:218.4px;height:308.5px}
.serif{font-family:"Libre Baskerville",Georgia,serif}
.sans{font-family:"Host Grotesk",Arial,sans-serif}
.title{font-family:"Libre Baskerville",Georgia,serif;font-size:13.5px;fill:var(--ink);text-anchor:middle}
.it{font-style:italic}
.mid{text-anchor:middle}
.end{text-anchor:end}
.c-navy{fill:var(--navy)} .c-orange{fill:var(--orange)} .c-blue{fill:var(--blue)}
.c-indigo{fill:var(--indigo)} .c-sky{fill:var(--sky)} .c-teal{fill:var(--teal)}
.c-cyan{fill:var(--cyan)} .c-purple{fill:var(--purple)} .c-plum{fill:var(--plum)}
.c-green{fill:var(--green)} .c-charcoal{fill:var(--charcoal)} .c-white{fill:#fff}
.c-ink{fill:var(--ink)} .c-track{fill:var(--track)}
.grid-line{stroke:var(--grid);stroke-width:.7;stroke-dasharray:2 2;fill:none}
.axis{stroke:var(--grid);stroke-width:1;fill:none}
.tick{font-family:"Host Grotesk",Arial,sans-serif;font-size:7px;fill:var(--ink)}
.val{font-family:"Host Grotesk",Arial,sans-serif;font-size:8px;fill:var(--ink)}
.lbl{font-family:"Host Grotesk",Arial,sans-serif;font-size:6.5px;fill:var(--ink)}
.big{font-family:"Host Grotesk",Arial,sans-serif;font-weight:500}
.arc{fill:none;stroke-width:7;stroke-linecap:round}
.leader{stroke:#b4b4bc;stroke-width:.7;fill:none}
.connector{stroke:var(--navy);stroke-width:2.5;fill:none}
.dotted{fill:none;stroke:var(--navy);stroke-width:1;stroke-dasharray:2 2}
.cell-code{font-family:"Libre Baskerville",Georgia,serif;font-size:12px}
.cell-note{font-family:"Host Grotesk",Arial,sans-serif;font-size:7px;fill:var(--ink)}
.cell-num{font-family:"Libre Baskerville",Georgia,serif;font-size:12.5px}
</style>
</head>
<body>
<main class="board">

<!-- Total deaths -->
<section class="panel" aria-label="Total overdose deaths 2024">
<svg viewBox="0 0 378 534">
  <text class="title" y="66"><tspan x="189"><tspan class="it">Total Death </tspan><tspan class="it c-orange">(2,595)</tspan> – Number of</tspan><tspan x="189" dy="15">overdose deaths in Australia in 2024</tspan></text>
  <g transform="rotate(-90 99 186)" fill="none" stroke-width="13">
    <circle cx="99" cy="186" r="50" stroke="var(--navy)" stroke-dasharray="116 314"/>
    <circle cx="99" cy="186" r="50" stroke="var(--indigo)" stroke-dasharray="47 314" stroke-dashoffset="-116"/>
    <circle cx="99" cy="186" r="50" stroke="var(--blue)" stroke-dasharray="88 314" stroke-dashoffset="-163"/>
    <circle cx="99" cy="186" r="50" stroke="var(--orange)" stroke-dasharray="63 314" stroke-dashoffset="-251"/>
  </g>
  <text class="big c-navy mid" x="99" y="194" font-size="21">2,595</text>
  <rect x="197" y="139" width="131" height="96" rx="9" fill="#fff" stroke="var(--sky)" stroke-width="1.2"/>
  <path d="M211 152c-2-3-6-1-5 2l5 5 5-5c1-3-3-5-5-2z" fill="none" stroke="var(--orange)" stroke-width="1"/>
  <text class="lbl"><tspan x="222" y="156">Unintentional overdose</tspan><tspan x="222" dy="8">deaths</tspan></text>
  <text class="big c-navy" x="207" y="194" font-size="26">78%</text>
  <text class="lbl" x="270" y="193" font-size="5">or</text>
  <text class="big c-orange" x="207" y="220" font-size="26">1768</text>
  <text class="lbl" x="279" y="220" font-size="6">deaths</text>
  <rect x="44" y="258" width="284" height="254" rx="30" fill="var(--blue)" role="img" aria-label="Map of Australia with states shaded by overdose deaths"/>
</svg>
</section>

<!-- Overdose vs population -->
<section class="panel" aria-label="Overdose versus population">
<svg viewBox="0 0 378 534">
  <text class="title" y="66"><tspan x="189" class="it">Overdose vs. Population -</tspan><tspan x="189" dy="15">Unintentional overdose deaths compared with</tspan><tspan x="189" dy="15">population growth 2001 – 2024</tspan></text>
  <text class="lbl" font-size="8"><tspan x="54" y="245">Unintentional overdose</tspan><tspan x="54" dy="9">deaths compared with</tspan><tspan x="54" dy="9">population growth</tspan><tspan x="54" dy="9">2001 – 2024</tspan></text>
  <path d="M66 318H170V378H66A30 30 0 0 1 66 318Z" class="c-blue"/>
  <text class="big c-white mid" x="99" y="346" font-size="24">2,091</text>
  <text class="lbl c-white mid" x="99" y="358" font-size="7.5" fill="#fff"><tspan x="99" style="fill:#fff">Unintentional</tspan><tspan x="99" dy="9" style="fill:#fff">overdose deaths</tspan></text>
  <rect x="161" y="217" width="16" height="175" rx="8" fill="#fff" stroke="var(--blue)" stroke-width="2.5"/>
  <line x1="169" y1="258" x2="169" y2="386" stroke="var(--blue)" stroke-width="1.5"/>
  <circle cx="169" cy="258" r="3.5" class="c-blue"/>
  <path d="M209 230H312A30 30 0 0 1 312 292H209Z" class="c-orange"/>
  <rect x="201" y="217" width="16" height="175" rx="8" fill="#fff" stroke="var(--orange)" stroke-width="2.5"/>
  <line x1="209" y1="306" x2="209" y2="386" stroke="var(--orange)" stroke-width="1.5"/>
  <circle cx="209" cy="306" r="3.5" class="c-orange"/>
  <text class="big c-white mid" x="277" y="264" font-size="19">27194300</text>
  <text class="lbl mid" x="277" y="276" font-size="7.5" style="fill:#fff">Population of Australia</text>
</svg>
</section>

<!-- Overdose vs road toll -->
<section class="panel" aria-label="Overdose versus road toll">
<svg viewBox="0 0 378 534">
  <text class="title" y="66"><tspan x="189"><tspan class="it">Overdose vs. Road Toll - </tspan>Overdose deaths</tspan><tspan x="189" dy="15">compared with the road toll 2001 – 2024</tspan></text>
  <polygon class="dotted" points="80,293 19,351 55,351 55,402"/>
  <polygon class="c-orange" points="84,297 23,355 59,355 59,410 114,427 114,355 144,355"/>
  <text class="big c-ink mid" x="84" y="284" font-size="17">1,307</text>
  <text class="sans c-ink mid" font-size="11"><tspan x="84" y="441">Road traffic</tspan><tspan x="84" dy="15">accident deaths</tspan></text>
  <polygon class="dotted" points="184,231 132,283 160,283 160,352"/>
  <polygon class="dotted" points="192,231 245,283 218,283 218,330"/>
  <polygon class="c-navy" points="188,235 136,287 164,287 164,362 214,342 214,287 241,287"/>
  <text class="big c-ink mid" x="188" y="224" font-size="17">2,091</text>
  <text class="sans c-ink mid" font-size="11"><tspan x="188" y="381">Unintentional</tspan><tspan x="188" dy="15">Overdose Deaths</tspan></text>
  <polygon class="dotted" points="298,173 355,232 325,232 325,290"/>
  <polygon class="c-blue" points="294,177 241,232 266,232 266,304 321,284 321,232 351,232"/>
  <text class="big c-ink mid" x="294" y="162" font-size="17">2,596</text>
  <text class="sans c-ink mid" font-size="11"><tspan x="294" y="324">All drug</tspan><tspan x="294" dy="15">induced deaths</tspan></text>
</svg>
</section>

<!-- Gender split -->
<section class="panel" aria-label="Gender split of unintentional overdose deaths">
<svg viewBox="0 0 378 534">
  <text class="title it" y="66"><tspan x="189">Gender split of</tspan><tspan x="189" dy="15">unintentional overdose deaths</tspan></text>
  <path d="M129 272A55 55 0 0 1 220 230H325" fill="none" stroke="var(--orange)" stroke-width="14"/>
  <polygon class="c-orange" points="325,214 343,230 325,246"/>
  <path d="M239 272A55 55 0 0 1 148 314H45" fill="none" stroke="var(--blue)" stroke-width="14"/>
  <polygon class="c-blue" points="45,298 27,314 45,330"/>
  <circle cx="185" cy="221" r="9" fill="#fff"/>
  <text class="big c-navy mid" x="185" y="225" font-size="10">F</text>
  <circle cx="219" cy="316" r="9" fill="#fff"/>
  <text class="big c-navy mid" x="219" y="320" font-size="10">M</text>
  <text class="serif it c-ink mid" font-size="7.5"><tspan x="184" y="266">Gender split of</tspan><tspan x="184" dy="9">unintentional</tspan><tspan x="184" dy="9">overdose deaths</tspan></text>
  <circle cx="81" cy="267" r="33" class="c-blue" role="img" aria-label="Illustration of a man"/>
  <text class="big c-ink mid" x="81" y="224" font-size="13">1520</text>
  <circle cx="288" cy="284" r="33" class="c-orange" role="img" aria-label="Illustration of a woman"/>
  <text class="big c-ink mid" x="290" y="338" font-size="13">571</text>
</svg>
</section>

<!-- Age group -->
<section class="panel" aria-label="Percent of unintentional overdose deaths by age group">
<svg viewBox="0 0 378 534">
  <text class="title it" y="66"><tspan x="189">Percent of unintentional</tspan><tspan x="189" dy="15">overdose deaths by age group</tspan></text>
  <g>
    <line class="grid-line" x1="40" y1="220" x2="355" y2="220"/><line class="grid-line" x1="40" y1="254" x2="355" y2="254"/>
    <line class="grid-line" x1="40" y1="287" x2="355" y2="287"/><line class="grid-line" x1="40" y1="319" x2="355" y2="319"/>
    <line class="grid-line" x1="40" y1="352" x2="355" y2="352"/><line class="grid-line" x1="40" y1="384" x2="355" y2="384"/>
    <line class="axis" x1="40" y1="419" x2="355" y2="419"/>
  </g>
  <g class="tick" font-size="6.5">
    <text x="22" y="222">25.5</text><text x="22" y="256">25.4</text><text x="22" y="289">17.1</text>
    <text x="22" y="321">13.4</text><text x="28" y="354">9</text><text x="24" y="386">8.6</text><text x="24" y="419">0.8</text>
  </g>
  <rect class="c-blue" x="52" y="407" width="29" height="12"/>
  <rect class="c-cyan" x="96" y="393" width="29" height="26"/>
  <rect class="c-teal" x="140" y="349" width="29" height="70"/>
  <rect class="c-sky" x="184" y="255" width="29" height="164"/>
  <rect class="c-teal" x="228" y="222" width="29" height="197"/>
  <rect class="c-blue" x="271" y="321" width="29" height="98"/>
  <rect class="c-cyan" x="313" y="353" width="29" height="66"/>
  <g class="tick mid" font-size="6.5">
    <text x="66" y="430">0-19</text><text x="110" y="430">20-29</text><text x="154" y="430">30-39</text>
    <text x="198" y="430">40-49</text><text x="242" y="430">50-59</text><text x="285" y="430">60-69</text>
    <text x="327" y="430">70 years</text><text x="327" y="437">and above</text>
  </g>
</svg>
</section>

<!-- Indigenous rates -->
<section class="panel" aria-label="Overdose death rates for Indigenous and non-Indigenous Australians">
<svg viewBox="0 0 378 534">
  <text class="title" y="67"><tspan x="189">Overdose death rates for</tspan><tspan x="189" dy="15" class="it">Indigenous and non-Indigenous Australians</tspan></text>
  <line class="axis" x1="52" y1="145" x2="52" y2="392"/>
  <line class="axis" x1="52" y1="392" x2="345" y2="392"/>
  <g class="tick end" font-size="6.5">
    <text x="47" y="151">30</text><text x="47" y="168">28</text><text x="47" y="184">26</text><text x="47" y="201">24</text>
    <text x="47" y="218">22</text><text x="47" y="234">20</text><text x="47" y="251">18</text><text x="47" y="268">16</text>
    <text x="47" y="284">14</text><text x="47" y="301">12</text><text x="47" y="318">10</text><text x="47" y="334">8</text>
    <text x="47" y="351">6</text><text x="47" y="368">4</text><text x="47" y="384">2</text>
  </g>
  <polyline fill="none" stroke="var(--orange)" stroke-width="2" points="71,285.4 97.2,262.2 123.4,252.2 149.6,249.7 175.8,255.5 202,232.2 228.2,246.3 254.4,236.4 280.6,215.6 306.8,221.4 333,154.8"/>
  <polyline fill="none" stroke="var(--blue)" stroke-width="2" points="71,347.8 97.2,343.7 123.4,343.7 149.6,342 175.8,341.2 202,344.5 228.2,345.4 254.4,346.2 280.6,346.2 306.8,349.5 333,343.7"/>
  <g fill="var(--ink)">
    <circle cx="71" cy="285.4" r="3"/><circle cx="97.2" cy="262.2" r="3"/><circle cx="123.4" cy="252.2" r="3"/><circle cx="149.6" cy="249.7" r="3"/>
    <circle cx="175.8" cy="255.5" r="3"/><circle cx="202" cy="232.2" r="3"/><circle cx="228.2" cy="246.3" r="3"/><circle cx="254.4" cy="236.4" r="3"/>
    <circle cx="280.6" cy="215.6" r="3"/><circle cx="306.8" cy="221.4" r="3"/><circle cx="333" cy="154.8" r="3"/>
    <circle cx="71" cy="347.8" r="3"/><circle cx="97.2" cy="343.7" r="3"/><circle cx="123.4" cy="343.7" r="3"/><circle cx="149.6" cy="342" r="3"/>
    <circle cx="175.8" cy="341.2" r="3"/><circle cx="202" cy="344.5" r="3"/><circle cx="228.2" cy="345.4" r="3"/><circle cx="254.4" cy="346.2" r="3"/>
    <circle cx="280.6" cy="346.2" r="3"/><circle cx="306.8" cy="349.5" r="3"/><circle cx="333" cy="343.7" r="3"/>
  </g>
  <g class="tick mid" font-size="6.5">
    <text x="65" y="279">13.6</text><text x="92" y="254">16.4</text><text x="118" y="244">17.6</text><text x="146" y="242">17.9</text>
    <text x="173" y="269">17.2</text><text x="200" y="226">20</text><text x="225" y="259">18.3</text><text x="251" y="229">19.5</text>
    <text x="278" y="208">22</text><text x="304" y="235">21.3</text><text x="330" y="148">29.3</text>
    <text x="68" y="360">6.1</text><text x="97" y="336">6.6</text><text x="123" y="336">6.6</text><text x="149" y="334">6.8</text>
    <text x="175" y="333">6.9</text><text x="198" y="357">6.5</text><text x="225" y="358">6.4</text><text x="251" y="359">6.3</text>
    <text x="277" y="359">6.3</text><text x="304" y="362">5.9</text><text x="330" y="336">6.6</text>
  </g>
  <g class="tick mid" font-size="6.5">
    <text x="71" y="405">2014</text><text x="97.2" y="405">2015</text><text x="123.4" y="405">2016</text><text x="149.6" y="405">2017</text>
    <text x="175.8" y="405">2018</text><text x="202" y="405">2019</text><text x="228.2" y="405">2020</text><text x="254.4" y="405">2021</text>
    <text x="280.6" y="405">2022</text><text x="306.8" y="405">2023</text><text x="333" y="405">2024</text>
  </g>
  <rect class="c-orange" x="118" y="429" width="7" height="7"/>
  <text class="lbl" x="131" y="436" font-size="7.5">Indigenous</text>
  <rect class="c-blue" x="184" y="429" width="7" height="7"/>
  <text class="lbl" x="197" y="436" font-size="7.5">Non-Indigenous</text>
</svg>
</section>

<!-- Opioid types -->
<section class="panel" aria-label="Deaths by opioid types">
<svg viewBox="0 0 378 534">
  <text class="title" y="67"><tspan x="189">Deaths by <tspan class="it">opioid types</tspan></tspan></text>
  <circle cx="151" cy="253" r="128" fill="none" stroke="#f1f1f4" stroke-width="4"/>
  <circle cx="151" cy="253" r="142" fill="none" stroke="#f4f4f6" stroke-width="3"/>
  <path class="leader" d="M151 303H271V278M151 318H304V296M151 331H274V327M151 343H302V358M151 355H258V370M151 368H200V377"/>
  <path class="arc" stroke="var(--navy)" d="M151 368A115 115 0 0 1 46.8 204.4"/>
  <path class="arc" stroke="var(--indigo)" d="M151 355A102 102 0 0 1 62.7 304"/>
  <path class="arc" stroke="var(--green)" d="M151 343A90 90 0 1 1 208.9 184.1"/>
  <path class="arc" stroke="var(--orange)" d="M151 331A78 78 0 0 1 148.3 175.1"/>
  <path class="arc" stroke="var(--blue)" d="M151 318A65 65 0 1 1 215.7 258.7"/>
  <path class="arc" stroke="var(--plum)" d="M151 303A50 50 0 0 1 133.9 206"/>
  <g class="tick" font-size="7">
    <text x="40" y="204">488</text><text x="158" y="187">236</text><text x="198" y="194">877</text>
    <text x="101" y="244">194</text><text x="203" y="272">370</text><text x="64" y="320">160</text>
  </g>
  <g class="lbl" font-size="4.6">
    <text x="272" y="272">Synthetics (inc. fentanyl,</text><text x="272" y="277">pethidine, tramadol)</text>
    <text x="302" y="293">Pharmaceutical opioids</text>
    <text x="283" y="322">Natural and semi-synthetics (inc.</text><text x="283" y="327">oxycodone, morphine, codeine)</text>
    <text x="304" y="356">Total opioids</text>
    <text x="248" y="370">Methadone</text>
    <text x="194" y="383">Heroin</text>
  </g>
</svg>
</section>

<!-- Polydrug -->
<section class="panel" aria-label="Polydrug versus single drug deaths 2020-2024">
<svg viewBox="0 0 378 534">
  <text class="title it" y="67"><tspan x="189">Polydrug vs single</tspan><tspan x="189" dy="15" style="font-style:normal">drug deaths 2020-2024</tspan></text>
  <path class="connector" d="M158 153V218M236 153V218M145 223H82Q69 223 69 236V257M69 338V355Q69 368 82 368H148M239 223H302Q315 223 315 236V256M315 336V355Q315 368 302 368H236"/>
  <g class="c-navy">
    <circle cx="158" cy="153" r="4"/><circle cx="236" cy="153" r="4"/><circle cx="69" cy="257" r="4"/>
    <circle cx="69" cy="338" r="4"/><circle cx="315" cy="256" r="4"/><circle cx="315" cy="336" r="4"/>
  </g>
  <circle cx="192" cy="293" r="82" class="c-navy"/>
  <text class="serif it mid" font-size="12" style="fill:#fff"><tspan x="192" y="281">Polydrug vs</tspan><tspan x="192" dy="15">single drug deaths</tspan><tspan x="192" dy="15">2020-2024</tspan></text>
  <circle cx="192" cy="171" r="30" class="c-indigo"/>
  <text class="lbl mid" font-size="5" style="fill:#fff"><tspan x="192" y="159">Single</tspan><tspan x="192" dy="6">Drug Type</tspan></text>
  <text class="big mid" x="192" y="182" font-size="14" style="fill:#fff">2,354</text>
  <circle cx="69" cy="298" r="30" class="c-blue"/>
  <text class="lbl mid" font-size="5" style="fill:#fff"><tspan x="69" y="287">Two</tspan><tspan x="69" dy="6">Drug Types</tspan></text>
  <text class="big mid" x="69" y="309" font-size="14" style="fill:#fff">1,340</text>
  <circle cx="315" cy="295" r="30" class="c-orange"/>
  <text class="lbl mid" font-size="5" style="fill:#fff"><tspan x="315" y="284">Three or more</tspan><tspan x="315" dy="6">Drug Type</tspan></text>
  <text class="big mid" x="315" y="306" font-size="14" style="fill:#fff">3,610</text>
</svg>
</section>

<!-- Drug type -->
<section class="panel" aria-label="Unintentional deaths by drug type">
<svg viewBox="0 0 378 534">
  <text class="title" y="67"><tspan x="189">Unintentional</tspan><tspan x="189" dy="15" class="it">deaths by drug type</tspan></text>
  <line class="axis" x1="281" y1="128" x2="281" y2="420"/>
  <line class="axis" x1="104" y1="420" x2="281" y2="420"/>
  <g stroke="var(--grid)" stroke-width=".8">
    <line x1="277" y1="155" x2="281" y2="155"/><line x1="277" y1="184" x2="281" y2="184"/><line x1="277" y1="213" x2="281" y2="213"/>
    <line x1="277" y1="242" x2="281" y2="242"/><line x1="277" y1="271" x2="281" y2="271"/><line x1="277" y1="300" x2="281" y2="300"/>
    <line x1="277" y1="329" x2="281" y2="329"/><line x1="277" y1="358" x2="281" y2="358"/><line x1="277" y1="387" x2="281" y2="387"/>
  </g>
  <g class="c-track">
    <rect x="112" y="115" width="8" height="305"/><rect x="131" y="115" width="8" height="305"/><rect x="148" y="115" width="8" height="305"/>
    <rect x="166" y="115" width="8" height="305"/><rect x="186" y="115" width="8" height="305"/><rect x="205" y="115" width="8" height="305"/>
    <rect x="224" y="115" width="8" height="305"/><rect x="243" y="115" width="8" height="305"/><rect x="262" y="115" width="8" height="305"/>
  </g>
  <rect class="c-orange" x="113" y="133" width="6" height="270" rx="3"/>
  <rect class="c-indigo" x="132" y="170" width="6" height="233" rx="3"/>
  <rect class="c-blue" x="149" y="187" width="6" height="216" rx="3"/>
  <rect class="c-navy" x="167" y="222" width="6" height="181" rx="3"/>
  <rect class="c-charcoal" x="187" y="240" width="6" height="163" rx="3"/>
  <rect class="c-purple" x="206" y="265" width="6" height="138" rx="3"/>
  <rect class="c-plum" x="225" y="273" width="6" height="130" rx="3"/>
  <rect class="c-green" x="244" y="292" width="6" height="111" rx="3"/>
  <rect class="c-blue" x="263" y="328" width="6" height="75" rx="3"/>
  <g class="tick" font-size="7">
    <text transform="translate(119 128) rotate(-90)">877</text>
    <text transform="translate(138 165) rotate(-90)">772</text>
    <text transform="translate(155 182) rotate(-90)">514</text>
    <text transform="translate(173 217) rotate(-90)">311</text>
    <text transform="translate(193 235) rotate(-90)">293</text>
    <text transform="translate(212 260) rotate(-90)">234</text>
    <text transform="translate(231 268) rotate(-90)">218</text>
    <text transform="translate(250 287) rotate(-90)">174</text>
    <text transform="translate(269 323) rotate(-90)">141</text>
  </g>
  <g class="tick" font-size="6.5">
    <text transform="translate(119 495) rotate(-90)">Opioids</text>
    <text transform="translate(138 495) rotate(-90)">Amphetamine</text>
    <text transform="translate(155 495) rotate(-90)">Benzodiazepines</text>
    <text transform="translate(173 495) rotate(-90)">Alcohol</text>
    <text transform="translate(193 495) rotate(-90)">Antidepressants</text>
    <text transform="translate(212 495) rotate(-90)">Anti-convulsants</text>
    <text transform="translate(231 495) rotate(-90)">Cannabinoids</text>
    <text transform="translate(250 495) rotate(-90)">Antipsychotics</text>
    <text transform="translate(269 495) rotate(-90)">Cocaine</text>
  </g>
</svg>
</section>

<!-- Ambulance -->
<section class="panel" aria-label="Ambulance attendances and GHB">
<svg viewBox="0 0 378 534">
  <text class="title" x="189" y="70">Ambulance attendances and GHB</text>
  <text class="title it" x="189" y="109" font-size="12">Ambulance Attendances 2024</text>
  <g class="grid-line">
    <line x1="113" y1="155" x2="113" y2="415"/><line x1="141" y1="155" x2="141" y2="415"/><line x1="169" y1="155" x2="169" y2="415"/>
    <line x1="197" y1="155" x2="197" y2="415"/><line x1="225" y1="155" x2="225" y2="415"/><line x1="253" y1="155" x2="253" y2="415"/>
    <line x1="281" y1="155" x2="281" y2="415"/><line x1="309" y1="155" x2="309" y2="415"/><line x1="337" y1="155" x2="337" y2="415"/>
  </g>
  <line class="axis" x1="85" y1="155" x2="85" y2="415"/>
  <rect class="c-blue" x="86" y="160" width="49" height="22"/>
  <rect class="c-navy" x="86" y="193" width="61" height="22"/>
  <rect class="c-purple" x="86" y="226" width="99" height="22"/>
  <rect class="c-sky" x="86" y="259" width="206" height="22"/>
  <rect class="c-plum" x="86" y="291" width="48" height="22"/>
  <rect class="c-indigo" x="86" y="324" width="245" height="22"/>
  <rect class="c-orange" x="86" y="356" width="39" height="22"/>
  <rect class="c-blue" x="86" y="387" width="48" height="22"/>
  <g class="serif it" font-size="11" style="fill:#fff">
    <text x="90" y="175">3500</text><text x="102" y="208">4376</text><text x="118" y="241">7081</text>
    <text x="163" y="274">14743</text><text x="90" y="306">3448</text><text x="183" y="339">17522</text>
    <text x="88" y="371">2767</text><text x="90" y="402">3443</text>
  </g>
  <g class="lbl end" font-size="5.8">
    <text x="79" y="173">All opioid analgesics</text><text x="79" y="206">Antidepressants</text><text x="79" y="239">Benzodiazepines</text>
    <text x="79" y="272">Amphetamines</text><text x="79" y="304">Cocaine</text><text x="79" y="337">Cannabinoids</text>
    <text x="79" y="369">Heroin</text><text x="79" y="400">GHB</text>
  </g>
  <g class="tick mid" font-size="5">
    <text x="85" y="429">0</text><text x="113" y="429">2000</text><text x="141" y="429">4000</text><text x="169" y="429">6000</text>
    <text x="197" y="429">8000</text><text x="225" y="429">10000</text><text x="253" y="429">12000</text><text x="281" y="429">14000</text>
    <text x="309" y="429">16000</text><text x="337" y="429">18000</text>
  </g>
  <text class="serif it mid c-ink" x="202" y="446" font-size="6.5">Number of Ambulance Attendances</text>
</svg>
</section>

<!-- Regional vs city -->
<section class="panel" aria-label="Regional deaths compared with city deaths">
<svg viewBox="0 0 378 534">
  <text class="title" x="189" y="69"><tspan class="it">Regional deaths </tspan>compared with city deaths</text>
  <g class="grid-line">
    <line x1="44" y1="138" x2="362" y2="138"/><line x1="44" y1="171" x2="362" y2="171"/><line x1="44" y1="204" x2="362" y2="204"/>
    <line x1="44" y1="237" x2="362" y2="237"/><line x1="44" y1="270" x2="362" y2="270"/><line x1="44" y1="303" x2="362" y2="303"/>
    <line x1="44" y1="336" x2="362" y2="336"/><line x1="44" y1="369" x2="362" y2="369"/>
  </g>
  <line class="axis" x1="44" y1="402" x2="362" y2="402"/>
  <g class="tick end" font-size="6.5">
    <text x="35" y="140">1600</text><text x="35" y="173">1400</text><text x="35" y="206">1200</text><text x="35" y="239">1000</text>
    <text x="35" y="272">800</text><text x="35" y="305">600</text><text x="35" y="338">400</text><text x="35" y="371">200</text><text x="35" y="404">0</text>
  </g>
  <g class="c-indigo">
    <rect x="48" y="196.4" width="8" height="205.6"/><rect x="102" y="185.5" width="8" height="216.5"/><rect x="157" y="192.4" width="8" height="209.6"/>
    <rect x="209" y="177.4" width="8" height="224.6"/><rect x="263" y="192.4" width="8" height="209.6"/><rect x="317" y="156.8" width="8" height="245.2"/>
  </g>
  <g class="c-blue">
    <rect x="59" y="350.8" width="8" height="51.2"/><rect x="113" y="350.2" width="8" height="51.8"/><rect x="168" y="351.7" width="8" height="50.3"/>
    <rect x="220" y="347.5" width="8" height="54.5"/><rect x="274" y="346.9" width="8" height="55.1"/><rect x="328" y="346.9" width="8" height="55.1"/>
  </g>
  <g class="c-orange">
    <rect x="70" y="375.3" width="8" height="26.7"/><rect x="124" y="379.4" width="8" height="22.6"/><rect x="179" y="377.4" width="8" height="24.6"/>
    <rect x="231" y="376.8" width="8" height="25.2"/><rect x="285" y="378.2" width="8" height="23.8"/><rect x="339" y="371.8" width="8" height="30.2"/>
  </g>
  <g class="c-navy">
    <rect x="80" y="397.2" width="8" height="4.8"/><rect x="134" y="396.2" width="8" height="5.8"/><rect x="189" y="396.7" width="8" height="5.3"/>
    <rect x="241" y="396.6" width="8" height="5.4"/><rect x="295" y="396.7" width="8" height="5.3"/><rect x="349" y="395.6" width="8" height="6.4"/>
  </g>
  <g class="tick mid" font-size="6.2">
    <text x="52" y="193">1246</text><text x="106" y="182">1312</text><text x="161" y="189">1270</text>
    <text x="213" y="174">1361</text><text x="267" y="189">1270</text><text x="321" y="153">1486</text>
    <text x="63" y="348">310</text><text x="117" y="347">314</text><text x="172" y="349">305</text><text x="224" y="345">330</text><text x="278" y="344">334</text><text x="332" y="344">334</text>
    <text x="74" y="372">162</text><text x="128" y="376">137</text><text x="183" y="374">149</text><text x="235" y="374">153</text><text x="289" y="375">144</text><text x="343" y="369">183</text>
    <text x="84" y="394">29</text><text x="138" y="393">35</text><text x="193" y="394">32</text><text x="245" y="394">33</text><text x="299" y="394">32</text><text x="353" y="393">39</text>
  </g>
  <g class="tick mid" font-size="7">
    <text x="66" y="418">2019</text><text x="120" y="418">2020</text><text x="175" y="418">2021</text>
    <text x="227" y="418">2022</text><text x="281" y="418">2023</text><text x="335" y="418">2024</text>
  </g>
  <rect x="35" y="442" width="236" height="48" fill="var(--row-a)"/>
  <rect class="c-indigo" x="47" y="452" width="7" height="7"/><rect class="c-orange" x="152" y="452" width="7" height="7"/>
  <rect class="c-blue" x="47" y="471" width="7" height="7"/><rect class="c-navy" x="152" y="471" width="7" height="7"/>
  <g class="serif it c-ink" font-size="5.2">
    <text x="59" y="458">Major Cities of Australia</text><text x="164" y="458">Outer Regional Australia</text>
    <text x="59" y="477">Inner Regional Australia</text><text x="164" y="477">Remote or Very Remote Australia</text>
  </g>
</svg>
</section>

<!-- Historic highs -->
<section class="panel" aria-label="Historic highs">
<svg viewBox="0 0 378 534">
  <text class="title" x="189" y="52">Historic highs</text>
  <rect x="32" y="82" width="314" height="29" class="c-blue"/>
  <text class="serif mid" x="132" y="101" font-size="11" style="fill:#fff">2024</text>
  <text class="serif mid" x="290" y="101" font-size="11" style="fill:#fff">2001</text>
  <rect x="32" y="111" width="314" height="84" fill="var(--row-a)"/>
  <rect x="32" y="195" width="314" height="76" fill="var(--row-b)"/>
  <rect x="32" y="271" width="314" height="77" fill="var(--row-a)"/>
  <rect x="32" y="348" width="314" height="80" fill="var(--row-b)"/>
  <rect x="32" y="428" width="314" height="76" fill="var(--row-a)"/>
  <g stroke="#fff" stroke-width="1"><line x1="134" y1="111" x2="134" y2="504"/><line x1="252" y1="111" x2="252" y2="504"/></g>
  <g class="cell-code c-navy"><text x="50" y="133">12A</text><text x="144" y="133">12B</text></g>
  <text class="cell-note"><tspan x="50" y="148">Most unintentional</tspan><tspan x="50" dy="8">drug-induced deaths</tspan></text>
  <text class="cell-note"><tspan x="144" y="148">Highest rate of unintentional</tspan><tspan x="144" dy="8">drug-induced deaths per</tspan><tspan x="144" dy="8">100,000 population</tspan></text>
  <text class="cell-num c-navy" x="50" y="172" font-weight="700">2091</text>
  <text class="cell-num c-navy" x="144" y="182">7.6</text>
  <g class="cell-code c-blue"><text x="50" y="212">12C</text><text x="144" y="212">12C</text></g>
  <text class="cell-note"><tspan x="50" y="227">Most unintentional</tspan><tspan x="50" dy="8">heroin deaths</tspan></text>
  <text class="cell-note"><tspan x="144" y="227">Most unintentional</tspan><tspan x="144" dy="8">amphetamine-type</tspan><tspan x="144" dy="8">stimulant deaths</tspan></text>
  <text class="cell-num c-blue" x="50" y="249">488</text>
  <text class="cell-num c-blue" x="144" y="259">772</text>
  <text class="cell-num c-navy mid" x="299" y="212">101</text>
  <text class="cell-code c-blue" x="50" y="294">12C</text>
  <text class="cell-note"><tspan x="50" y="309">Most unintentional</tspan><tspan x="50" dy="8">cocaine deaths</tspan></text>
  <text class="cell-num c-blue" x="50" y="330">141</text>
  <text class="cell-num c-navy mid" x="299" y="294">53</text>
  <g class="cell-code c-blue"><text x="50" y="367">12D</text><text x="144" y="367">12D</text></g>
  <text class="cell-note"><tspan x="50" y="382">Most unintentional</tspan><tspan x="50" dy="8">drug-induced deaths</tspan><tspan x="50" dy="8">in VIC</tspan></text>
  <text class="cell-note"><tspan x="144" y="382">Most unintentional</tspan><tspan x="144" dy="8">drug-induced deaths in QLD</tspan></text>
  <text class="cell-num c-blue" x="50" y="412">572</text>
  <text class="cell-num c-blue" x="144" y="404">417</text>
  <g class="cell-code c-blue"><text x="50" y="448">12D</text><text x="144" y="448">12D</text></g>
  <text class="cell-note"><tspan x="50" y="463">Most unintentional</tspan><tspan x="50" dy="8">drug-induced deaths</tspan><tspan x="50" dy="8">in WA</tspan></text>
  <text class="cell-note"><tspan x="144" y="463">Most unintentional</tspan><tspan x="144" dy="8">drug-induced deaths in SA</tspan></text>
  <text class="cell-num c-blue" x="50" y="493">278</text>
  <text class="cell-num c-blue" x="144" y="486">157</text>
</svg>
</section>

<!-- Causes of death -->
<section class="panel" aria-label="Leading causes of death aged 20 to 59">
<svg viewBox="0 0 378 534">
  <text class="title" x="189" y="69">Causes of Death (20-59)</text>
  <text class="title it" x="189" y="89" font-size="12.5">Leading causes of death aged 20 - 59</text>
  <path class="c-navy" d="M191 303L110.4 353.4A95 95 0 0 1 161.6 212.7Z"/>
  <path class="c-orange" d="M191 303L279.3 350A100 100 0 0 1 106.2 356Z"/>
  <path class="c-purple" d="M191 303L156.4 196.5A112 112 0 0 1 289.9 355.6Z"/>
  <text class="big mid" x="229" y="266" font-size="24" style="fill:#fff">2367</text>
  <text class="lbl mid" font-size="7" style="fill:#fff"><tspan x="229" y="280">Intentional self-harm</tspan><tspan x="229" dy="8">(suicide)</tspan></text>
  <text class="big mid" x="138" y="293" font-size="21" style="fill:#fff">1339</text>
  <text class="lbl mid" font-size="7" style="fill:#fff"><tspan x="138" y="303">Accidental</tspan><tspan x="138" dy="8">poisoning: drug</tspan></text>
  <text class="big mid" x="193" y="356" font-size="22" style="fill:#fff">1550</text>
  <text class="lbl mid" font-size="7" style="fill:#fff"><tspan x="193" y="368">Ischaemic heart</tspan><tspan x="193" dy="8">diseases</tspan></text>
</svg>
</section>

<!-- Deaths by state -->
<section class="panel" aria-label="Deaths by state">
<svg viewBox="0 0 378 534">
  <text class="title" x="189" y="69">Deaths by State</text>
  <text class="title it" x="189" y="89" font-size="12.5">NSW and VIC lead national volume</text>
  <g class="grid-line">
    <line x1="40" y1="200" x2="358" y2="200"/><line x1="40" y1="232.7" x2="358" y2="232.7"/><line x1="40" y1="265.3" x2="358" y2="265.3"/>
    <line x1="40" y1="298" x2="358" y2="298"/><line x1="40" y1="330.7" x2="358" y2="330.7"/><line x1="40" y1="363.3" x2="358" y2="363.3"/>
  </g>
  <line class="axis" x1="40" y1="396" x2="358" y2="396"/>
  <g class="tick end" font-size="6.5">
    <text x="28" y="202">600</text><text x="28" y="235">500</text><text x="28" y="267">400</text><text x="28" y="300">300</text>
    <text x="28" y="333">200</text><text x="28" y="365">100</text><text x="28" y="398">0</text>
  </g>
  <rect class="c-blue" x="53" y="391.1" width="27" height="4.9"/>
  <rect class="c-cyan" x="93" y="386.5" width="27" height="9.5"/>
  <rect class="c-teal" x="132" y="384.6" width="27" height="11.4"/>
  <rect class="c-sky" x="171" y="344.7" width="27" height="51.3"/>
  <rect class="c-teal" x="210" y="305.2" width="27" height="90.8"/>
  <rect class="c-blue" x="249" y="259.8" width="27" height="136.2"/>
  <rect class="c-purple" x="288" y="209.1" width="27" height="186.9"/>
  <rect class="c-orange" x="327" y="204.2" width="27" height="191.8"/>
  <g class="val mid">
    <text x="66" y="386">15</text><text x="106" y="382">29</text><text x="145" y="380">35</text><text x="184" y="340">157</text>
    <text x="223" y="300">278</text><text x="262" y="255">417</text><text x="301" y="205">572</text><text x="340" y="200">587</text>
  </g>
  <g class="tick mid" font-size="6">
    <text x="66" y="413">NT</text><text x="106" y="413">ACT</text><text x="145" y="413">TAS</text><text x="184" y="413">SA</text>
    <text x="223" y="413">WA</text><text x="262" y="413">QLD</text><text x="301" y="413">VIC</text><text x="340" y="413">NSW</text>
  </g>
</svg>
</section>

<!-- Cocaine trend -->
<section class="panel" aria-label="Cocaine death trend">
<svg viewBox="0 0 378 534">
  <text class="title" x="189" y="82">Cocaine Death Trend</text>
  <g stroke="#d9dbe4" stroke-width=".7">
    <line x1="49" y1="204.4" x2="334" y2="204.4"/><line x1="49" y1="222.7" x2="334" y2="222.7"/><line x1="49" y1="241.1" x2="334" y2="241.1"/>
    <line x1="49" y1="259.4" x2="334" y2="259.4"/><line x1="49" y1="277.8" x2="334" y2="277.8"/><line x1="49" y1="296.2" x2="334" y2="296.2"/>
    <line x1="49" y1="314.5" x2="334" y2="314.5"/><line x1="49" y1="332.9" x2="334" y2="332.9"/><line x1="49" y1="351.2" x2="334" y2="351.2"/>
    <line x1="49" y1="369.6" x2="334" y2="369.6"/>
    <line x1="66" y1="186" x2="66" y2="388"/><line x1="84" y1="186" x2="84" y2="388"/><line x1="101.9" y1="186" x2="101.9" y2="388"/>
    <line x1="120" y1="186" x2="120" y2="388"/><line x1="137.7" y1="186" x2="137.7" y2="388"/><line x1="155.6" y1="186" x2="155.6" y2="388"/>
    <line x1="173.6" y1="186" x2="173.6" y2="388"/><line x1="191.5" y1="186" x2="191.5" y2="388"/><line x1="209.4" y1="186" x2="209.4" y2="388"/>
    <line x1="227.4" y1="186" x2="227.4" y2="388"/><line x1="245.3" y1="186" x2="245.3" y2="388"/><line x1="263.2" y1="186" x2="263.2" y2="388"/>
    <line x1="281.2" y1="186" x2="281.2" y2="388"/><line x1="299" y1="186" x2="299" y2="388"/><line x1="317" y1="186" x2="317" y2="388"/>
  </g>
  <rect x="49" y="186" width="285" height="202" fill="none" stroke="#8d90a0" stroke-width=".8"/>
  <g class="tick end" font-size="6.5">
    <text x="41" y="188">150</text><text x="41" y="207">100</text><text x="41" y="225">95</text><text x="41" y="243">90</text>
    <text x="41" y="262">85</text><text x="41" y="280">80</text><text x="41" y="298">75</text><text x="41" y="317">70</text>
    <text x="41" y="335">65</text><text x="41" y="353">60</text><text x="41" y="372">55</text><text x="41" y="390">50</text>
  </g>
  <polyline fill="none" stroke="var(--orange)" stroke-width="1.3" points="66,366 101.9,287 137.7,222 173.6,208 209.4,197 245.3,212 281.2,194 317,189"/>
  <g class="c-orange">
    <circle cx="66" cy="366" r="2.6"/><circle cx="101.9" cy="287" r="2.6"/><circle cx="137.7" cy="222" r="2.6"/><circle cx="173.6" cy="208" r="2.6"/>
    <circle cx="209.4" cy="197" r="2.6"/><circle cx="245.3" cy="212" r="2.6"/><circle cx="281.2" cy="194" r="2.6"/><circle cx="317" cy="189" r="2.6"/>
  </g>
  <g class="serif c-ink mid" font-size="7">
    <text x="58" y="369">55</text><text x="95" y="289">77</text><text x="137" y="216">95</text><text x="170" y="202">99</text>
    <text x="207" y="191">110</text><text x="247" y="222">97</text><text x="280" y="189">110</text><text x="320" y="199">141</text>
  </g>
  <g class="tick mid" font-size="6.8">
    <text x="66" y="404">2017</text><text x="101.9" y="404">2018</text><text x="137.7" y="404">2019</text><text x="173.6" y="404">2020</text>
    <text x="209.4" y="404">2021</text><text x="245.3" y="404">2022</text><text x="281.2" y="404">2023</text><text x="317" y="404">2024</text>
  </g>
</svg>
</section>

</main>
</body>
</html>
```